Business Card Design Project

Hi Designers, this project is currently on hold until the Logo is completed:
Please submit to the Logo project here:
http://jobs.pixelmarket.example/job.aspx?id=371905

Once logo is completed, it will be attached to this project for you to create business cards with show logo, company name and address

Maren T K Ashdown

Corwin's Meadow Pine Flock Co.
Hazelmere
Upper Brackwell
North Devon EX21 4TN

Tel: 01809 351846
Mobile: 07912 463078
email: maren@meadow-pine-flock.example
Updates

Project Deadline Extended
Reason: Sorry everyone, we have had a sick ewe and I am now behind with this one and need to extend the deadline. Best wishes Maren

The designer who wins the logo brief will be asked to design the business card. Many thanks Maren

Project Deadline Extended
Reason: Sorry everyone, just a chaotic time of year with animals. Need to extend the deadline again..... as I just haven't had enough time to take a good look.... Thank you for your understanding. Maren

Project Deadline Extended
Reason: Sorry everyone It is our busiest time of year with animals and just no time to spend going through such great designs. I will have to extend the deadline again and hopefully have some news very soon. Wishing you all a very happy Christmas and a happy and healthy new year. Maren & Corwin

Target Market(s)

High end market
Boutique restaurants for meat (it's not commercial lamb it's a slow matured quality meat more like venison/beef) expensive - specialized market

High End shoot clothing / wool / sheepskin rugs
Quality products

Industry/Entity Type

Business

Requirements
Must have
• based on the logo - (which Pixel Market has just been asked to do)
possibly based on a simplified picture of a Hebridean Ram (shows it's a Hebridean by it's horns as opposed to other black sheep!!)

```html
<!DOCTYPE html>
<html lang="en">
<head>
<meta charset="utf-8">
<title>Corwin's Meadow Pine Flock Co. – Business Card</title>
<link href="https://fonts.googleapis.com/css2?family=Lato:wght@400;700;900&display=swap" rel="stylesheet">
<style>
  :root {
    --page: #ecebe8;
    --teal-light: #2bb3d3;
    --teal: #1591b8;
    --teal-deep: #0b6a91;
    --paper: #ffffff;
    --paper-shade: #eeeeee;
    --leaf: #7aa84a;
    --sky: #1a7fa8;
    --ink: #1f2326;
    --cream: #f4f8ec;
  }
  * { margin: 0; padding: 0; box-sizing: border-box; }
  html, body { width: 1200px; height: 1023px; overflow: hidden; }
  body {
    background: var(--page);
    font-family: "Lato", Arial, sans-serif;
    position: relative;
  }
  .card {
    position: absolute;
    left: 270px;
    width: 660px;
    height: 378px;
    border-radius: 26px;
    overflow: hidden;
    box-shadow: 0 14px 30px rgba(0,0,0,0.18);
  }
  /* Front */
  .card-front {
    top: 82px;
    background: linear-gradient(150deg, var(--teal-deep) 0%, var(--teal) 45%, var(--teal-light) 100%);
    display: flex;
    flex-direction: column;
    align-items: center;
    justify-content: center;
    gap: 18px;
  }
  .brand-mark {
    display: flex;
    align-items: center;
    gap: 12px;
  }
  .brand-dot {
    width: 22px; height: 22px;
    border-radius: 50%;
    background: var(--cream);
  }
  .brand-name {
    color: var(--cream);
    font-weight: 900;
    font-size: 28px;
  }
  .tagline {
    color: var(--paper);
    font-weight: 700;
    font-size: 24px;
  }
  /* Back */
  .card-back {
    top: 562px;
    background: linear-gradient(160deg, var(--paper) 0%, var(--paper) 55%, var(--paper-shade) 100%);
  }
  .company {
    position: absolute;
    top: 34px;
    right: 250px;
    text-align: right;
  }
  .company-name {
    color: var(--leaf);
    font-weight: 700;
    font-size: 22px;
    margin-bottom: 14px;
  }
  .address {
    color: var(--sky);
    font-weight: 700;
    font-size: 20px;
    line-height: 1.25;
    font-style: normal;
  }
  .contact {
    position: absolute;
    left: 40px;
    top: 190px;
    list-style: none;
    font-size: 19px;
    line-height: 1.3;
    font-weight: 700;
    color: var(--ink);
  }
  .contact .label { color: var(--sky); }
  .contact .email { font-weight: 400; }
  .side-panel {
    position: absolute;
    right: 0; top: 0;
    width: 220px; height: 100%;
    background: linear-gradient(180deg, var(--teal-light), var(--teal-deep));
    display: flex;
    align-items: center;
    justify-content: center;
    padding: 20px;
  }
  .side-panel .brand-name {
    font-size: 20px;
    text-align: center;
    line-height: 1.3;
  }
  .person {
    position: absolute;
    right: 250px;
    bottom: 34px;
    font-size: 21px;
    font-weight: 700;
    color: var(--ink);
  }
</style>
</head>
<body>
  <section class="card card-front" aria-label="Business card front">
    <div class="brand-mark">
      <span class="brand-dot"></span>
      <span class="brand-name">Corwin's Meadow Pine Flock Co.</span>
    </div>
    <p class="tagline">Quality products</p>
  </section>

  <section class="card card-back" aria-label="Business card back">
    <div class="company">
      <p class="company-name">Corwin's Meadow Pine Flock Co.</p>
      <address class="address">
        Hazelmere<br>
        Upper Brackwell<br>
        North Devon EX21 4TN
      </address>
    </div>
    <ul class="contact">
      <li><span class="label">Tel:</span> 01809 351846</li>
      <li><span class="label">Mob:</span> 07912 463078</li>
      <li class="email"><span class="label">email:</span> maren@meadow-pine-flock.example</li>
    </ul>
    <p class="person">Maren T K Ashdown</p>
    <div class="side-panel" role="img" aria-label="Brand mark area">
      <span class="brand-name">Corwin's Meadow Pine Flock Co.</span>
    </div>
  </section>
</body>
</html>
```